Car wrap design for Boxwarden

We need a car wrap design for our Van (Velmora Tarsk Hi roof Black color). We are freight expert sending international parcels from China to New Zealand. Consonlidating parcels and save money for customers. We would like to see designs that use the color match our logo and final design should communicate our service and tell customer we are expert,Specializing in International Freight Forwarding within China's Trade Line.

Our website: www.boxwarden.co.nz Our phone: 09 4813096, We specialized: Sea Parcels, Air Parcels, Loose Cargo
in China Trade line

Target Market(s)

New Zealand small business

Industry/Entity Type

International Freight Fowarding

• Please refer to brand guideline

Requirements
Must have
• logo, website, phone, what we do (Sea Parcels, Air Parcels, Loose Cargo)
Nice to have
• Beautiful Lines or Graphics

```html
<!DOCTYPE html>
<html lang="en">
<head>
<meta charset="utf-8">
<title>Boxwarden van wrap – right side</title>
<link rel="stylesheet" href="https://fonts.googleapis.com/css2?family=Anton&family=Arimo:wght@400&family=Roboto+Condensed:wght@300&display=swap">
<style>
  :root {
    --amber: #f0a500;
    --brick: #a6241f;
    --signal-red: #d9261e;
    --ink: #1e1a17;
    --mist-grey: #bdbdbd;
    --paper: #ffffff;
  }
  html, body {
    margin: 0;
    padding: 0;
    overflow: hidden;
    background: var(--paper);
  }
  .wrap-sheet {
    position: relative;
    width: 1200px;
    height: 782px;
    overflow: hidden;
    background: var(--paper);
  }
  .side-label {
    position: absolute;
    left: 429px;
    top: 56px;
    margin: 0;
    font-family: "Arimo", Arial, sans-serif;
    font-weight: 400;
    font-size: 92px;
    line-height: 1;
    color: var(--ink);
  }
  .livery-graphic {
    position: absolute;
    left: 0;
    top: 0;
    width: 1200px;
    height: 782px;
  }
  .services {
    position: absolute;
    left: 160px;
    top: 492px;
    margin: 0;
    padding: 0;
    list-style: none;
    font-family: "Anton", "Arial Narrow", sans-serif;
    color: var(--ink);
  }
  .services li {
    font-size: 20px;
    line-height: 21px;
    letter-spacing: 0.2px;
  }
  .services .trade-line {
    font-size: 14px;
    line-height: 20px;
    margin-top: 1px;
  }
  .brand-name {
    position: absolute;
    left: 506px;
    top: 533px;
    margin: 0;
    font-family: "Anton", "Arial Narrow", sans-serif;
    font-weight: 400;
    font-size: 92px;
    line-height: 1.1;
    letter-spacing: -1px;
    color: var(--signal-red);
  }
  .website {
    position: absolute;
    left: 670px;
    top: 513px;
    font-family: "Roboto Condensed", "Arial Narrow", sans-serif;
    font-weight: 300;
    font-size: 25px;
    line-height: 1;
    color: var(--mist-grey);
  }
  .phone {
    position: absolute;
    left: 917px;
    top: 492px;
    font-family: "Anton", "Arial Narrow", sans-serif;
    font-size: 44px;
    line-height: 1.1;
    letter-spacing: 0.5px;
    color: var(--mist-grey);
  }
</style>
</head>
<body>
<main class="wrap-sheet">
  <h1 class="side-label">Right Side</h1>

  <svg class="livery-graphic" viewBox="0 0 1200 782" role="img" aria-label="Amber and brick-red diagonal livery graphic with stripes and halftone texture">
    <defs>
      <radialGradient id="livery-warmth" cx="110" cy="670" r="620" gradientUnits="userSpaceOnUse">
        <stop offset="0" stop-color="#a6241f"/>
        <stop offset="0.28" stop-color="#c8541a"/>
        <stop offset="0.55" stop-color="#f0a500"/>
        <stop offset="1" stop-color="#f0a500"/>
      </radialGradient>
    </defs>
    <polygon points="84,237 838,697 84,697" fill="url(#livery-warmth)"/>
  </svg>

  <ul class="services">
    <li>Sea Parcels</li>
    <li>Air Parcels</li>
    <li>Loose Cargo</li>
    <li class="trade-line">Transport in China Trade Line</li>
  </ul>

  <p class="brand-name">BOXWARDEN</p>
  <span class="website">www.boxwarden.co.nz</span>
  <span class="phone">09 4813096</span>
</main>
</body>
</html>
```